Volunteer fire fighters needed banner

As part of our recruitment campaign, we need a sign we can post on our sign trailer to entice locals to join our volunteer fire service. This design will be printed on a banner, front and back, to catch traffic going in both directions on a busy roadway. This banner will have a printed surface of 4 feet tall by 8 feet long.
Our fire department is looking to attract people between the ages of 18 and 35 years old who are interested in being a firefighter. We offer our volunteers:
-Free professional training
-All equipment supplied
-Tax abatements for active volunteers
For more information, you can check us out at:
Brookmerecrestfire.example

This design should:
-scale to and fit a 4'x8' canvas
-Include our web address "BrookmereCrestFire.example"
-Say "Members Wanted"
-"Drill every Tuesday at 7pm"
-"37 Quarry Bend Lane"
-Include "Brookmere Crest Fire Department"

We've included reference photos and past images we use for our other campaigns for inspiration for you.

Target Market(s)

18-35 y/o

Industry/Entity Type

Fire Service

Requirements
Must have
• -scale to and fit a 4'x8' canvas -Include our web address "BrookmereCrestFire.example" -Say "Members Wanted" -"Drill every Tuesday at 7pm" -"37 Quarry Bend Lane" -Include "Brookmere Crest Fire Department"

```html
<!DOCTYPE html>
<html lang="en">
<head>
<meta charset="utf-8">
<title>Brookmere Crest Fire Department – Members Wanted</title>
<link href="https://fonts.googleapis.com/css2?family=Poppins:wght@400;500;600;700;800&display=swap" rel="stylesheet">
<style>
  :root{
    --red:#e31b23;
    --navy:#233a74;
    --gold:#f0b21a;
    --sky:#3fa9f5;
    --white:#ffffff;
    --page:#eef0f3;
  }
  *{box-sizing:border-box;margin:0;padding:0}
  html,body{width:1200px;height:1117px;overflow:hidden;background:var(--page)}
  body{font-family:"Poppins",sans-serif;position:relative}
  .banner{position:absolute;left:0;top:274px;width:1200px;height:568px;background:var(--white);overflow:hidden}

  .top-band{position:absolute;left:0;top:0;width:100%;height:135px;background:var(--red)}
  .top-band .dept{position:absolute;left:60px;top:32px;color:var(--white);font-weight:600;font-size:24px;line-height:1;letter-spacing:1.2px;text-transform:uppercase}
  .top-band .headline{position:absolute;left:58px;top:58px;color:var(--white);font-weight:800;font-size:68px;line-height:1;letter-spacing:.5px;text-transform:uppercase}

  .truck-photo{position:absolute;left:0;top:135px;width:768px;height:302px;
    background:linear-gradient(100deg,#cfd0cc 0%,#b63a36 30%,#d42a2a 55%,#a8191c 75%,#e4e2de 100%)}

  .offer-frame{position:absolute;left:712px;top:14px;width:488px;height:382px;background:var(--white);
    clip-path:polygon(64px 0,100% 0,100% 100%,64px 100%,0 54%)}
  .offer-panel{position:absolute;left:727px;top:50px;width:473px;height:346px;background:var(--navy);
    clip-path:polygon(52px 0,100% 0,100% 100%,52px 100%,0 48%)}
  .offer-panel .offer-title{position:absolute;left:78px;top:46px;color:var(--gold);font-weight:700;font-size:21px;line-height:1;letter-spacing:.4px;text-transform:uppercase;white-space:nowrap}
  .offer-list{position:absolute;left:78px;top:84px;width:340px;list-style:none;color:var(--white);font-size:20px;line-height:22px}
  .offer-list li{position:relative;padding-left:26px;margin-bottom:11px}
  .offer-list li::before{content:"";position:absolute;left:0;top:5px;border-left:11px solid var(--red);border-top:6px solid transparent;border-bottom:6px solid transparent}
  .offer-panel .divider{position:absolute;left:78px;top:212px;width:336px;height:1px;background:var(--white);opacity:.85}
  .offer-panel .more{position:absolute;left:78px;top:224px;width:330px;color:var(--white);font-weight:700;font-size:19px;line-height:24px}
  .offer-panel .offer-url{position:absolute;left:78px;top:278px;color:var(--gold);font-weight:700;font-size:18px;line-height:1;white-space:nowrap}

  .lower-navy{position:absolute;left:0;top:437px;width:360px;height:115px;background:var(--navy)}
  .drill-band{position:absolute;left:360px;top:396px;width:840px;height:82px;background:var(--white)}
  .drill-band .drill{position:absolute;left:32px;top:22px;color:var(--red);font-weight:800;font-size:40px;line-height:1;text-transform:uppercase;white-space:nowrap}
  .info-band{position:absolute;left:360px;top:478px;width:840px;height:74px;background:var(--navy)}
  .info-band .site{position:absolute;left:34px;top:20px;color:var(--white);font-weight:700;font-size:24px;line-height:1;white-space:nowrap}
  .address-tab{position:absolute;left:872px;top:490px;width:328px;height:62px;background:var(--gold);border-radius:22px 0 0 0}
  .address-tab span{position:absolute;left:28px;top:18px;color:var(--navy);font-weight:700;font-size:22px;line-height:1;white-space:nowrap}
  .gold-strip{position:absolute;left:0;top:552px;width:100%;height:16px;background:var(--gold)}

  .dept-mark{position:absolute;left:158px;top:300px;width:228px;height:256px;background:var(--navy);border:5px solid var(--gold);border-radius:48px 48px 10px 10px;display:flex;flex-direction:column;align-items:center;justify-content:center;gap:14px;text-align:center}
  .dept-mark .dot{width:64px;height:64px;border-radius:50%;background:var(--red)}
  .dept-mark p{color:var(--gold);font-weight:700;font-size:18px;line-height:22px}

  .event-mark{position:absolute;left:22px;top:446px;width:126px;display:flex;flex-direction:column;align-items:center;gap:6px;text-align:center;color:var(--sky);font-weight:700;text-transform:uppercase}
  .event-mark .event-name{font-size:11px;line-height:13px}
  .event-mark .dot{width:44px;height:44px;border-radius:50%;background:var(--red)}
  .event-mark .event-kind{font-size:13px;line-height:14px}

  .side-mark{position:absolute;left:1012px;top:410px;width:172px;display:flex;align-items:center;gap:8px}
  .side-mark .dot{flex:none;width:28px;height:28px;border-radius:50%;background:var(--gold)}
  .side-mark p{color:var(--red);font-weight:700;font-size:15px;line-height:18px}
</style>
</head>
<body>
  <section class="banner">
    <div class="top-band">
      <p class="dept">Brookmere Crest Fire Department</p>
      <h1 class="headline">Members Wanted</h1>
    </div>
    <div class="truck-photo" role="img" aria-label="Photo of red fire engines parked inside the station bay"></div>
    <div class="offer-frame"></div>
    <div class="offer-panel">
      <p class="offer-title">We offer our volunteers:</p>
      <ul class="offer-list">
        <li>Free professional training</li>
        <li>All equipment supplied</li>
        <li>Tax abatements for active volunteers</li>
      </ul>
      <div class="divider"></div>
      <p class="more">For more information, you can check us out at:</p>
      <p class="offer-url">www.Brookmerecrestfire.example</p>
    </div>
    <div class="lower-navy"></div>
    <div class="drill-band"><p class="drill">Drill every Tuesday at 7pm</p></div>
    <div class="info-band"><p class="site">www.Brookmerecrestfire.example</p></div>
    <div class="address-tab"><span>37 Quarry Bend Lane</span></div>
    <div class="gold-strip"></div>
    <div class="event-mark">
      <p class="event-name">Hal Porter Memorial</p>
      <div class="dot"></div>
      <p class="event-kind">Egg Hunt</p>
    </div>
    <div class="dept-mark">
      <div class="dot"></div>
      <p>Brookmere Crest Fire Dept</p>
    </div>
    <div class="side-mark">
      <div class="dot"></div>
      <p>Brookmere Crest</p>
    </div>
  </section>
</body>
</html>
```